professional business card design

Business card design. Photos have been uploaded and i am open to the designer choosing which photos to use. Would like the card to be mostyly in a grey scale design with black, whites, silver & grey colours. I have added copy of our flyer as would like on the back side of card our services to be listed. Do not use any bright colurs such as blue red green or yellow. i need to be able to edit the phone number and naem in the final card design submitted.

Target Market(s)

Clients

Industry/Entity Type

earhmovibng and transport

Contact Information for Business Card

Director Name, address, email, phone number and services

Colors

Designer to choose only greyscale colors for use in the design.

Requirements
Should not have
• no yellow, red, blue or green

```html
<!DOCTYPE html>
<html lang="en">
<head>
<meta charset="utf-8">
<title>Karrow Haul Pty Ltd – Business Card</title>
<link href="https://fonts.googleapis.com/css2?family=Rajdhani:wght@500;600;700&family=Exo+2:wght@500;600&display=swap" rel="stylesheet">
<style>
  :root{
    --page:#e4e3e1;
    --card:#050506;
    --card-glow:#2a2b2e;
    --white:#f4f4f4;
    --silver:#c9c9c9;
    --grey:#8d8d8d;
    --dark-grey:#5a5a5a;
    --rule:#9a9a9a;
  }
  *{margin:0;padding:0;box-sizing:border-box}
  html,body{width:1200px;height:1200px;overflow:hidden;background:var(--page)}
  .canvas{position:relative;width:1200px;height:1200px}
  .card{
    position:absolute;left:239px;width:723px;height:413px;border-radius:20px;overflow:hidden;
    background:radial-gradient(ellipse 45% 70% at 50% 55%, var(--card-glow) 0%, #121315 45%, var(--card) 80%);
    box-shadow:0 3px 8px rgba(0,0,0,.25);
    color:var(--white);
  }
  .card--front{top:140px}
  .card--back{top:645px}

  /* front */
  .brand{position:absolute;left:40px;top:150px;width:290px;text-align:center;font-family:"Rajdhani",sans-serif}
  .brand__name{font-size:44px;font-weight:700;color:var(--silver);line-height:1;letter-spacing:1px}
  .brand__suffix{font-size:44px;font-weight:700;color:var(--silver);line-height:1.1;display:block}
  .divider{position:absolute;left:361px;top:114px;width:2px;height:175px;background:linear-gradient(var(--rule),var(--grey))}
  .person{position:absolute;left:396px;top:110px;font-family:"Rajdhani",sans-serif}
  .person__name{font-size:31px;font-weight:700;line-height:1.1;color:var(--white);letter-spacing:.5px}
  .person__role{font-size:22px;font-weight:500;color:var(--grey);letter-spacing:1px;line-height:1}
  .contacts{position:absolute;left:400px;top:200px;list-style:none;font-family:"Rajdhani",sans-serif;font-size:18px;font-weight:500;color:var(--white)}
  .contacts li{display:flex;align-items:center;height:36px;letter-spacing:.4px}
  .contacts svg{width:12px;height:12px;margin-right:10px;fill:var(--silver)}

  /* back */
  .services__title{position:absolute;left:0;right:0;top:44px;text-align:center;font-family:"Rajdhani",sans-serif;font-weight:700;font-size:32px;letter-spacing:7px;
    background:linear-gradient(90deg,var(--dark-grey),var(--silver) 50%,var(--grey));-webkit-background-clip:text;background-clip:text;color:transparent}
  .services{position:absolute;top:94px;list-style:none;font-family:"Exo 2",sans-serif;font-weight:600;font-size:16px;letter-spacing:1px;color:var(--white)}
  .services--left{left:62px}
  .services--right{left:423px}
  .services li{display:flex;align-items:center;height:23.2px;white-space:nowrap}
  .services svg{width:14px;height:14px;margin-right:10px;fill:none;stroke:var(--silver);stroke-width:2.6;stroke-linecap:round;stroke-linejoin:round}
  .services .indent{padding-left:24px}
  .fleet-photo{position:absolute;left:90px;top:250px;width:556px;height:127px;
    background:linear-gradient(180deg,#3a3b3d 0%,#2a2a2c 55%,#111 100%);
    -webkit-mask-image:radial-gradient(ellipse 60% 90% at 50% 50%,#000 60%,transparent 100%);
    mask-image:radial-gradient(ellipse 60% 90% at 50% 50%,#000 60%,transparent 100%)}
</style>
</head>
<body>
<main class="canvas">
  <section class="card card--front">
    <div class="brand">
      <span class="brand__name">KARROW HAUL</span>
      <span class="brand__suffix" style="font-size:22px;color:var(--silver);font-weight:700">Pty Ltd</span>
    </div>
    <div class="divider"></div>
    <div class="person">
      <h1 class="person__name">Yourname Here</h1>
      <p class="person__role">Designation</p>
    </div>
    <ul class="contacts">
      <li><svg viewBox="0 0 24 24"><path d="M6.6 10.8a15.1 15.1 0 0 0 6.6 6.6l2.2-2.2c.3-.3.7-.4 1-.2 1.1.4 2.3.6 3.6.6.6 0 1 .4 1 1V20c0 .6-.4 1-1 1A17 17 0 0 1 3 4c0-.6.4-1 1-1h3.5c.6 0 1 .4 1 1 0 1.2.2 2.4.6 3.6.1.3 0 .7-.2 1z"/></svg>000-123-456-789</li>
      <li><svg viewBox="0 0 24 24"><path d="M2 5h20v14H2zM3.5 6.5 12 12l8.5-5.5"/><path d="M3 6l9 6 9-6" stroke="#050506" stroke-width="2" fill="none"/></svg>youremail@email.com</li>
      <li><svg viewBox="0 0 24 24"><path d="M12 2a7 7 0 0 0-7 7c0 5.2 7 13 7 13s7-7.8 7-13a7 7 0 0 0-7-7zm0 9.5A2.5 2.5 0 1 1 12 6.5a2.5 2.5 0 0 1 0 5z"/></svg>123 St. Somewhere City</li>
    </ul>
  </section>

  <section class="card card--back">
    <h2 class="services__title">OUR SERVICES</h2>
    <ul class="services services--left">
      <li><svg viewBox="0 0 24 24"><path d="M4 13l5 5L20 6"/></svg>Over size loads / Hot Shot Loads</li>
      <li><svg viewBox="0 0 24 24"><path d="M4 13l5 5L20 6"/></svg>Heavy Vehicle Recovery Services</li>
      <li><svg viewBox="0 0 24 24"><path d="M4 13l5 5L20 6"/></svg>Potable Water Deliveries</li>
      <li><svg viewBox="0 0 24 24"><path d="M4 13l5 5L20 6"/></svg>Road Building / Maintenance</li>
      <li><svg viewBox="0 0 24 24"><path d="M4 13l5 5L20 6"/></svg>Earthworks</li>
      <li><svg viewBox="0 0 24 24"><path d="M4 13l5 5L20 6"/></svg>Sand &amp; Metal Supply &amp; Cartage</li>
    </ul>
    <ul class="services services--right">
      <li><svg viewBox="0 0 24 24"><path d="M4 13l5 5L20 6"/></svg>Road Train Tippers</li>
      <li><svg viewBox="0 0 24 24"><path d="M4 13l5 5L20 6"/></svg>Road Train Tankers</li>
      <li><svg viewBox="0 0 24 24"><path d="M4 13l5 5L20 6"/></svg>Road Train Flat Tops</li>
      <li><svg viewBox="0 0 24 24"><path d="M4 13l5 5L20 6"/></svg>Drop Deck Trailers</li>
      <li><svg viewBox="0 0 24 24"><path d="M4 13l5 5L20 6"/></svg>Mine Site accredited</li>
      <li class="indent">equipment &amp; Operators</li>
    </ul>
    <div class="fleet-photo" role="img" aria-label="Black and white photo of a road train with three tipper trailers on a dirt road"></div>
  </section>
</main>
</body>
</html>
```